Design a Chart Graphic that can be animated in video

We are looking for a clean and professional chart graphic that can be used on our website and edited to come alive in a video animation. The chart is to demonstrate that our product was proven to work in a clinical study. The chart title is Clinically Proven to Improve Sleep Quality. The x axis starts at "placebo" and ends at "tova calm" the placebo starts at 2% and the tova calm is 29% - the chart would show the rise from 2% to 29% in a dramatic way. The y axis would go from 0 - 30 %. There would be some sort of arrow to demonstrate the growth. Please see drawing for more clarity.

Target Market(s)

This is a study on SLEEP, the target market is sleep deprived men and women between the ages of 35-55.

Font styles to use
Sans Serif

Colors
0456a4
85abd2
85acd3
cedeed
ffffff
f04a50
fbed22

Requirements
Must have
• The chart must be delivered in a vector and styled in a way that can be animated by our video team. We are open to either flat or 3-D styles. The chart will be used on website and in video. It needs to look clean and professional, not funny or cartoonish. The color pallet needs to match www.itovacalm.com
• Please deliver vector, JPEG and PNG of the chart with and without a title.
Nice to have
• Fresh ideas to how to represent the chart in the most compelling way
Should not have
• Cartoons, gimmicky, colors other than those that match our website.

```html
<!DOCTYPE html>
<html lang="en">
<head>
<meta charset="utf-8">
<title>Clinically Proven to Improve Sleep Quality – chart set</title>
<link rel="stylesheet" href="https://fonts.googleapis.com/css2?family=Arimo:wght@700&display=swap">
<style>
  :root {
    --brand-blue: #0456a4;
    --mid-blue: #85abd2;
    --steel-blue: #5a88ba;
    --pale-blue: #cedeed;
    --white: #ffffff;
    --coral: #f04a50;
  }
  html, body {
    margin: 0;
    padding: 0;
    width: 1200px;
    height: 1200px;
    overflow: hidden;
  }
  .chart-grid {
    display: grid;
    grid-template-columns: 600px 600px;
    grid-template-rows: 600px 600px;
    width: 1200px;
    height: 1200px;
  }
  .tile { width: 600px; height: 600px; }
  .tile svg { display: block; width: 600px; height: 600px; }
  .tile--light { background: var(--white); }
  .tile--dark { background: var(--brand-blue); }

  .bar-track { fill: none; stroke-width: 3; }
  .tile--light .bar-track { stroke: var(--brand-blue); }
  .tile--dark .bar-track { stroke: var(--white); }

  .bar-value--placebo { fill: var(--pale-blue); }
  .bar-value--low { fill: var(--mid-blue); }
  .bar-value--mid { fill: var(--steel-blue); }
  .bar-value--product { fill: var(--brand-blue); }
  .tile--dark .bar-value--product { fill: var(--white); opacity: 0.9; }

  .growth-arrow {
    fill: var(--coral);
    stroke: var(--white);
    stroke-width: 3;
    stroke-linejoin: round;
  }

  .axis-label, .category-label {
    font-family: "Arimo", Arial, sans-serif;
    font-weight: 700;
    font-size: 14px;
  }
  .tile--light .axis-label { fill: var(--coral); }
  .tile--light .category-label--placebo { fill: var(--pale-blue); }
  .tile--light .category-label--product { fill: var(--brand-blue); }
  .tile--dark .axis-label,
  .tile--dark .category-label { fill: var(--white); }
</style>
</head>
<body>
<main class="chart-grid">

  <!-- Light, labelled -->
  <section class="tile tile--light">
    <svg viewBox="0 0 600 600" role="img" aria-label="Sleep quality improvement: placebo 2%, tova calm 29%">
      <g class="bars">
        <rect class="bar-value bar-value--placebo" x="166" y="411" width="62" height="19"/>
        <rect class="bar-value bar-value--low" x="241" y="336" width="62" height="94"/>
        <rect class="bar-value bar-value--mid" x="316" y="251" width="62" height="179"/>
        <rect class="bar-value bar-value--product" x="391" y="156" width="62" height="274"/>
        <rect class="bar-track" x="166" y="147" width="62" height="283"/>
        <rect class="bar-track" x="241" y="147" width="62" height="283"/>
        <rect class="bar-track" x="316" y="147" width="62" height="283"/>
        <rect class="bar-track" x="391" y="147" width="62" height="283"/>
      </g>
      <polygon class="growth-arrow" points="178.6,393.6 387.5,184.7 378.3,175.5 425,160 409.5,206.7 400.3,197.5 191.4,406.4"/>
      <text class="axis-label" x="126" y="155">30%</text>
      <text class="axis-label" x="126" y="294">15%</text>
      <text class="axis-label" x="126" y="434">0%</text>
      <text class="category-label category-label--placebo" x="163" y="455">PLACEBO</text>
      <text class="category-label category-label--product" x="455" y="455" text-anchor="end">TOVA CALM</text>
    </svg>
  </section>

  <!-- Dark, unlabelled -->
  <section class="tile tile--dark">
    <svg viewBox="0 0 600 600" role="img" aria-label="Sleep quality improvement chart">
      <g transform="translate(600,-4) translate(-600,0)">
        <rect class="bar-value bar-value--placebo" x="166" y="411" width="62" height="19"/>
        <rect class="bar-value bar-value--low" x="241" y="336" width="62" height="94"/>
        <rect class="bar-value bar-value--mid" x="316" y="251" width="62" height="179"/>
        <rect class="bar-track" x="166" y="147" width="62" height="283"/>
        <rect class="bar-track" x="241" y="147" width="62" height="283"/>
        <rect class="bar-track" x="316" y="147" width="62" height="283"/>
        <rect class="bar-track" x="391" y="147" width="62" height="283"/>
        <polygon class="growth-arrow" points="178.6,393.6 387.5,184.7 378.3,175.5 425,160 409.5,206.7 400.3,197.5 191.4,406.4"/>
      </g>
    </svg>
  </section>

  <!-- Dark, labelled -->
  <section class="tile tile--dark">
    <svg viewBox="0 0 600 600" role="img" aria-label="Sleep quality improvement: placebo 2%, tova calm 29%">
      <rect class="bar-value bar-value--placebo" x="166" y="411" width="62" height="19"/>
      <rect class="bar-value bar-value--low" x="241" y="336" width="62" height="94"/>
      <rect class="bar-value bar-value--mid" x="316" y="251" width="62" height="179"/>
      <rect class="bar-track" x="166" y="147" width="62" height="283"/>
      <rect class="bar-track" x="241" y="147" width="62" height="283"/>
      <rect class="bar-track" x="316" y="147" width="62" height="283"/>
      <rect class="bar-track" x="391" y="147" width="62" height="283"/>
      <polygon class="growth-arrow" points="178.6,393.6 387.5,184.7 378.3,175.5 425,160 409.5,206.7 400.3,197.5 191.4,406.4"/>
      <text class="axis-label" x="126" y="155">30%</text>
      <text class="axis-label" x="126" y="294">15%</text>
      <text class="axis-label" x="126" y="434">0%</text>
      <text class="category-label" x="163" y="455">PLACEBO</text>
      <text class="category-label" x="455" y="455" text-anchor="end">TOVA CALM</text>
    </svg>
  </section>

  <!-- Light, unlabelled -->
  <section class="tile tile--light">
    <svg viewBox="0 0 600 600" role="img" aria-label="Sleep quality improvement chart">
      <rect class="bar-value bar-value--placebo" x="166" y="411" width="62" height="19"/>
      <rect class="bar-value bar-value--low" x="241" y="336" width="62" height="94"/>
      <rect class="bar-value bar-value--mid" x="316" y="251" width="62" height="179"/>
      <rect class="bar-value bar-value--product" x="391" y="156" width="62" height="274"/>
      <rect class="bar-track" x="166" y="147" width="62" height="283"/>
      <rect class="bar-track" x="241" y="147" width="62" height="283"/>
      <rect class="bar-track" x="316" y="147" width="62" height="283"/>
      <rect class="bar-track" x="391" y="147" width="62" height="283"/>
      <polygon class="growth-arrow" points="178.6,393.6 387.5,184.7 378.3,175.5 425,160 409.5,206.7 400.3,197.5 191.4,406.4"/>
    </svg>
  </section>

</main>
</body>
</html>
```